Flyer for tutoring

The text should be presented in an engaging way to attract potential customers.
Colorfully designed
Around the edge, various objects related to school and the subjects (see text) should be visible.

```html
<!DOCTYPE html>
<html lang="de">
<head>
<meta charset="utf-8">
<title>Nachhilfe Flyer</title>
<link rel="stylesheet" href="https://fonts.googleapis.com/css2?family=Luckiest+Guy&family=Bitter:wght@400;600;700&display=swap">
<style>
  :root {
    --bg: #b3b3b3;
    --paper: #e9e8ea;
    --green: #3a9b3a;
    --blue: #2f4fb0;
    --magenta: #a32a6b;
    --pink: #d8006e;
    --teal: #1f8a8f;
    --orange: #e0611c;
    --violet: #6a0fd6;
    --ink: #1a1a1a;
    --wood-light: #efdcc0;
    --wood-dark: #d9bf98;
  }
  * { margin: 0; padding: 0; box-sizing: border-box; }
  html, body { width: 1200px; height: 493px; overflow: hidden; }
  body {
    background: var(--bg);
    font-family: "Bitter", Georgia, serif;
    display: flex;
    justify-content: center;
    align-items: flex-start;
    gap: 60px;
    padding-top: 30px;
  }
  .side { display: flex; flex-direction: column; align-items: center; gap: 18px; }
  .side-label {
    font-family: Arial, Helvetica, sans-serif;
    font-weight: 700; font-size: 14px; letter-spacing: 1px; color: var(--ink);
  }
  .flyer {
    position: relative;
    width: 283px; height: 400px;
    background: var(--paper);
    overflow: hidden;
    text-align: center;
  }
  .pencil-photo {
    position: absolute; left: 0; right: 0; bottom: 0; height: 140px;
    background: linear-gradient(180deg, rgba(233,232,234,0) 0%, var(--wood-light) 30%, var(--wood-dark) 100%);
  }
  .intro {
    position: absolute; top: 40px; left: 40px; right: 40px;
    color: var(--green); font-size: 10px; line-height: 1.05; font-weight: 600;
  }
  .headline {
    position: absolute; top: 86px; left: 14px; right: 14px;
    font-family: "Luckiest Guy", "Arial Black", sans-serif;
    color: var(--blue); font-size: 24px; line-height: 1.08; letter-spacing: 0.3px;
  }
  .tagline {
    position: absolute; top: 185px; left: 40px; right: 40px;
    font-family: "Luckiest Guy", "Arial Black", sans-serif;
    color: var(--magenta); font-size: 9.5px; line-height: 1.15;
  }
  .body-copy {
    position: absolute; left: 54px; right: 54px;
    font-size: 6.5px; line-height: 1.05;
  }
  .front .body-copy { top: 218px; color: var(--teal); }
  .badge {
    position: absolute; border-radius: 50%;
    display: flex; flex-direction: column; justify-content: center; align-items: center;
    color: #fff; text-align: center;
  }
  .badge-call {
    width: 83px; height: 83px; right: 34px; top: 273px; background: var(--pink);
    font-family: "Luckiest Guy", "Arial Black", sans-serif;
    transform: rotate(10deg);
  }
  .badge-call .small { font-size: 7.5px; line-height: 1.05; }
  .badge-call .number { font-size: 14px; line-height: 1; margin-top: 3px; }
  .badge-greet {
    width: 83px; height: 83px; right: 34px; top: 248px; background: var(--violet);
    font-size: 7px; font-weight: 700; line-height: 1.2; padding: 0 12px;
    transform: rotate(12deg);
  }
  .back .intro-orange { top: 40px; color: var(--orange); }
  .back .body-copy.intro-orange { left: 44px; right: 44px; }
  .back .lead { top: 89px; color: var(--magenta); }
  .motivation-band {
    position: absolute; top: 107px; left: 30px; width: 224px; height: 42px;
    background: var(--pink); color: #fff;
    font-family: "Luckiest Guy", "Arial Black", sans-serif;
    font-size: 10.5px; line-height: 1.25;
    display: flex; flex-direction: column; justify-content: center;
    transform: rotate(-2deg);
  }
  .back .about { top: 156px; color: var(--magenta); left: 48px; right: 48px; }
  .contact {
    position: absolute; top: 203px; left: 40px; right: 40px;
    color: var(--teal); font-size: 8.5px; line-height: 1.2;
  }
  .contact strong { font-weight: 700; }
</style>
</head>
<body>

<section class="side">
  <article class="flyer front">
    <div class="pencil-photo" role="img" aria-label="Photo of a row of sharpened coloured pencils"></div>
    <p class="intro">Möchtest du dich gerne in der Schule verbessern und suchst eine</p>
    <h1 class="headline">Professionelle Nachhilfelehreri n/Lerncoach</h1>
    <p class="tagline">Dann lass es uns doch mal versuchen!</p>
    <p class="body-copy">Die erste Lektion – die Kennenlernlektion – dauert ca. 30 Minuten. Sie ist kostenlos. Denn wir müssen ja sicher gehen, dass wir uns verstehen und leiden können. Bei unserem ersten Treffen legen wir auch fest, woran wir arbeiten werden und wann die Nachhilfe in deine Agenda passt.</p>
    <div class="badge badge-call">
      <span class="small">Kontaktiere<br>n Sie mich</span>
      <span class="number">079 214<br>58 73</span>
    </div>
  </article>
  <span class="side-label">FRONT</span>
</section>

<section class="side">
  <article class="flyer back">
    <div class="pencil-photo" role="img" aria-label="Photo of a row of sharpened coloured pencils"></div>
    <p class="body-copy intro-orange">Die erste Lektion – die Kennenlernlektion – dauert ca. 30 Minuten. Sie ist kostenlos. Denn wir müssen ja sicher gehen, dass wir uns verstehen und leiden können. Bei unserem ersten Treffen legen wir auch fest, woran wir arbeiten werden und wann die Nachhilfe in deine Agenda passt.</p>
    <p class="body-copy lead">Wenn der erste Eindruck stimmt, dann legen wir los, und bald schon werden</p>
    <div class="motivation-band"><span>Deine Motivation und</span><span>deine Noten besser und besser!</span></div>
    <p class="body-copy about"><strong>Zu meiner Person:</strong> Ich wohne hier in der Siedlung Lindenweg und bin ausgebildete und sehr erfahrene Sekundar- und Primarlehrerin in den Fächern Deutsch, Französisch, Englisch und Geschichte. (Auf Wunsch auch Mathe-Nachhilfe möglich.)</p>
    <p class="contact">
      <strong>Meine Kontaktdaten:</strong><br>
      <strong>Mail:</strong> lena.berger@postfach.ch<br>
      <strong>Tel.</strong> 079 214 58 73 (nachmittags fast immer erreichbar)
    </p>
    <div class="badge badge-greet">Ich freue mich auf deine Kontaktaufnah me! Bis bald!</div>
  </article>
  <span class="side-label">BACK</span>
</section>

</body>
</html>
```